Redesign Video/PIcture Check in Page

Redesign our current TetherWatchApp iPhone App checkin screens - Keep the design simple so that programmers do not have to do too much extra work to make your design work. - Look at the attached website screenshot for the overall look and feel, and color scheme - Convert the attached vector logo to iOS Icon format. - Deliver all graphics in the density required for iPhone XS Max. I will upload current check in pages that need to be reimagined. Check in needs to be more intutitive. Would like to add some gamification to the verification screen where they currently are required to enter series of random numbers. simple card game etc might work better. See TetherWatchapp in itunes and google play store. also visit quorvant-link.example or tetherwatchapp.example for more information about our company.
The Current Checkin Process:
A. Client receives alert to checkin or submits voluntary checkin
B. Clicks checkin button on home Screen.
Redesign from here:
C. Clicks on a check in from check in list screen(new screen)
D. Enters verification number(gamification something better than random numbers)
E. Opens Camera
D. Takes Selfie
F. submits photo
G. clicks check in
SEE CURRENT STEPS PIC I UPLOADED

Target Market(s)

Courts,Probation and parole,Attorneys,Sheriffs,Jails, Alternative sentencing

Colors
3277b5

Requirements
Must have
• Must be easy to navigate,Intuitive!
Nice to have
• Gamification of check in verification.
• Step by step process with next button or similar

```html
<!DOCTYPE html>
<html lang="en">
<head>
<meta charset="utf-8">
<title>Check-ins</title>
<link href="https://fonts.googleapis.com/css2?family=Nunito+Sans:wght@400;600;700&display=swap" rel="stylesheet">
<style>
  :root {
    --bg-top: #2f7ab9;
    --bg-bottom: #3c4ca2;
    --card: rgba(58, 108, 178, 0.82);
    --card-border: rgba(255, 255, 255, 0.28);
    --divider: rgba(255, 255, 255, 0.22);
    --text: #ffffff;
    --text-muted: rgba(255, 255, 255, 0.42);
    --check-bg: #24589e;
    --fab-ring: #a9b3dc;
    --fab-icon: #3a62ad;
  }
  * { box-sizing: border-box; margin: 0; padding: 0; }
  html, body { width: 675px; height: 1200px; overflow: hidden; }
  body {
    font-family: "Nunito Sans", "Helvetica Neue", Arial, sans-serif;
    color: var(--text);
    background: linear-gradient(180deg, var(--bg-top) 0%, #3566b0 50%, var(--bg-bottom) 100%);
    position: relative;
  }
  .status-bar {
    position: absolute; top: 0; left: 0; right: 0; height: 54px;
    display: flex; align-items: center; justify-content: space-between;
    padding: 0 20px; font-size: 19px; font-weight: 400;
  }
  .status-left, .status-right { display: flex; align-items: center; gap: 8px; }
  .signal { display: flex; gap: 3px; }
  .signal span { width: 9px; height: 9px; border-radius: 50%; background: var(--text); }
  .signal span.off { background: transparent; border: 1px solid var(--text); }
  .app-header {
    position: absolute; top: 66px; left: 0; right: 0; height: 40px;
    display: flex; align-items: center; justify-content: center;
  }
  .app-header h1 { font-size: 20px; font-weight: 700; letter-spacing: 0.3px; }
  .menu-btn { position: absolute; left: 22px; top: 8px; }
  .next-btn { position: absolute; right: 22px; top: 9px; }
  .checkin-card {
    position: absolute; left: 22px; top: 133px; width: 634px; height: 942px;
    background: var(--card); border: 1px solid var(--card-border); border-radius: 12px;
    list-style: none;
  }
  .checkin-item {
    position: relative; height: 127px; margin: 0 23px;
    border-bottom: 1.5px solid var(--divider);
  }
  .checkin-date { position: absolute; top: 38px; left: 0; font-size: 15px; color: var(--text-muted); }
  .checkin-title { position: absolute; top: 62px; left: 0; font-size: 20.5px; font-weight: 600; }
  .checkin-status {
    position: absolute; right: 0; top: 46px; width: 47px; height: 47px;
    border-radius: 9px; background: var(--check-bg);
    display: flex; align-items: center; justify-content: center;
  }
  .tab-bar {
    position: absolute; left: 0; right: 0; top: 1100px; height: 100px;
  }
  .tab {
    position: absolute; top: 10px; width: 120px; margin-left: -60px;
    display: flex; flex-direction: column; align-items: center;
    font-size: 17px; font-weight: 600;
  }
  .tab svg { height: 28px; margin-bottom: 8px; }
  .tab-home { left: 62px; }
  .tab-checkins { left: 205px; }
  .tab-map { left: 448px; }
  .tab-howto { left: 610px; }
  .fab {
    position: absolute; left: 303px; top: 9px; width: 72px; height: 72px;
    border-radius: 50%; background: #ffffff; border: 5px solid var(--fab-ring);
    display: flex; align-items: center; justify-content: center;
  }
</style>
</head>
<body>
  <div class="status-bar">
    <div class="status-left">
      <div class="signal"><span></span><span></span><span></span><span></span><span class="off"></span></div>
      <span>Carrier</span>
      <svg width="20" height="15" viewBox="0 0 20 15"><path d="M10 14 L13 10.5 A4.5 4.5 0 0 0 7 10.5 Z" fill="#fff"/><path d="M3.5 7.5 A9 9 0 0 1 16.5 7.5" stroke="#fff" stroke-width="2.2" fill="none"/><path d="M0.8 4.3 A13 13 0 0 1 19.2 4.3" stroke="#fff" stroke-width="2.2" fill="none"/></svg>
    </div>
    <div class="status-right">
      <svg width="18" height="18" viewBox="0 0 18 18"><circle cx="9" cy="9" r="7.5" stroke="#fff" stroke-width="1.6" fill="none"/><rect x="5.8" y="8" width="6.4" height="4.8" rx="1" fill="#fff"/><path d="M7 8 V6.5 A2 2 0 0 1 11 6.5 V8" stroke="#fff" stroke-width="1.4" fill="none"/></svg>
      <span>100%</span>
      <svg width="44" height="18" viewBox="0 0 44 18"><rect x="1" y="1" width="38" height="16" rx="3" stroke="#fff" stroke-width="1.6" fill="none"/><rect x="3.5" y="3.5" width="33" height="11" rx="1.5" fill="#fff"/><rect x="40.5" y="6" width="2.5" height="6" rx="1" fill="#fff"/></svg>
    </div>
  </div>

  <header class="app-header">
    <svg class="menu-btn" width="31" height="23" viewBox="0 0 31 23" aria-label="Menu"><g fill="#fff"><rect x="0" y="0" width="4" height="4"/><rect x="8" y="0.5" width="23" height="3"/><rect x="0" y="9.5" width="4" height="4"/><rect x="8" y="10" width="23" height="3"/><rect x="0" y="19" width="4" height="4"/><rect x="8" y="19.5" width="23" height="3"/></g></svg>
    <h1>CHECK-INS</h1>
    <svg class="next-btn" width="14" height="24" viewBox="0 0 14 24" aria-label="Next"><path d="M2.5 2.5 L11.5 12 L2.5 21.5" stroke="#fff" stroke-width="3.4" fill="none" stroke-linecap="round" stroke-linejoin="round"/></svg>
  </header>

  <ul class="checkin-card">
    <li class="checkin-item"><span class="checkin-date">20 Nov 2018 10: 47 : 59</span><span class="checkin-title">Voluntary Check-in Request</span><span class="checkin-status"><svg width="26" height="20" viewBox="0 0 26 20"><path d="M3 10.5 L10 17 L23 3.5" stroke="#fff" stroke-width="3.6" fill="none" stroke-linecap="round" stroke-linejoin="round"/></svg></span></li>
    <li class="checkin-item"><span class="checkin-date">20 Nov 2018 10: 47 : 59</span><span class="checkin-title">Voluntary Check-in Request</span><span class="checkin-status"><svg width="26" height="20" viewBox="0 0 26 20"><path d="M3 10.5 L10 17 L23 3.5" stroke="#fff" stroke-width="3.6" fill="none" stroke-linecap="round" stroke-linejoin="round"/></svg></span></li>
    <li class="checkin-item"><span class="checkin-date">20 Nov 2018 10: 47 : 59</span><span class="checkin-title">Voluntary Check-in Request</span><span class="checkin-status"><svg width="26" height="20" viewBox="0 0 26 20"><path d="M3 10.5 L10 17 L23 3.5" stroke="#fff" stroke-width="3.6" fill="none" stroke-linecap="round" stroke-linejoin="round"/></svg></span></li>
    <li class="checkin-item"><span class="checkin-date">20 Nov 2018 10: 47 : 59</span><span class="checkin-title">Voluntary Check-in Request</span><span class="checkin-status"><svg width="26" height="20" viewBox="0 0 26 20"><path d="M3 10.5 L10 17 L23 3.5" stroke="#fff" stroke-width="3.6" fill="none" stroke-linecap="round" stroke-linejoin="round"/></svg></span></li>
    <li class="checkin-item"><span class="checkin-date">20 Nov 2018 10: 47 : 59</span><span class="checkin-title">Voluntary Check-in Request</span><span class="checkin-status"><svg width="26" height="20" viewBox="0 0 26 20"><path d="M3 10.5 L10 17 L23 3.5" stroke="#fff" stroke-width="3.6" fill="none" stroke-linecap="round" stroke-linejoin="round"/></svg></span></li>
    <li class="checkin-item"><span class="checkin-date">20 Nov 2018 10: 47 : 59</span><span class="checkin-title">Voluntary Check-in Request</span><span class="checkin-status"><svg width="26" height="20" viewBox="0 0 26 20"><path d="M3 10.5 L10 17 L23 3.5" stroke="#fff" stroke-width="3.6" fill="none" stroke-linecap="round" stroke-linejoin="round"/></svg></span></li>
    <li class="checkin-item"><span class="checkin-date">20 Nov 2018 10: 47 : 59</span><span class="checkin-title">Voluntary Check-in Request</span><span class="checkin-status"><svg width="26" height="20" viewBox="0 0 26 20"><path d="M3 10.5 L10 17 L23 3.5" stroke="#fff" stroke-width="3.6" fill="none" stroke-linecap="round" stroke-linejoin="round"/></svg></span></li>
  </ul>

  <nav class="tab-bar">
    <div class="tab tab-home"><svg width="28" height="28" viewBox="0 0 28 28"><path d="M14 4 L26 15 H22.5 V25 H17 V18.5 H11 V25 H5.5 V15 H2 Z" fill="#fff"/></svg>Home</div>
    <div class="tab tab-checkins"><svg width="32" height="28" viewBox="0 0 32 28"><path d="M4 15 L12 22.5 L28 5.5" stroke="#fff" stroke-width="4.5" fill="none" stroke-linecap="round" stroke-linejoin="round"/></svg>Check-ins</div>
    <div class="fab"><svg width="26" height="26" viewBox="0 0 26 26"><path d="M13 2 V24 M2 13 H24" stroke="var(--fab-icon)" stroke-width="2.6" stroke-linecap="round"/></svg></div>
    <div class="tab tab-map"><svg width="22" height="28" viewBox="0 0 22 28"><path d="M11 27 C11 27 2 16 2 10 A9 9 0 0 1 20 10 C20 16 11 27 11 27 Z" fill="#fff"/><circle cx="11" cy="10" r="3.5" fill="#3a5aa8"/></svg>Map</div>
    <div class="tab tab-howto"><svg width="16" height="28" viewBox="0 0 16 28"><circle cx="10" cy="3.5" r="3.2" fill="#fff"/><path d="M3 11 H11 L8 24 H12 L11.5 27 H2 L5 14 H2.5 Z" fill="#fff"/></svg>How To</div>
  </nav>
</body>
</html>
```